Velora Pedalworks

We are a new start up company selling (online) innovative cycling products.
Being a new player in the market a modern eye catching logo would be good.
Initially selling safety tail lights with blinkers & modern designed cycling gloves and eventually extending our range into cycling clothing. Many of our products will have a safety theme.

Please see logo attached.

Reason: I have extended deadline because i have just received the Logo to be used.

Target Market(s)

We will be target marketing to the young 20-30year old trendy commuter cyclists to the 40 - 60 year old weekend road riders with there immaculate color coordinated road bikes & clothing.

Industry/Entity Type

Safety

Requirements
Must have
• Name: Mavin Tolby
Line for Mobile No. 0438 261 905
Line for email Address: mavin@velorapedalworks.example.com.au
3 Lines for Postal Address: PO Box 3862
Wattle Crest Corner
NSW 2174
Website: www.velorapedalworks.example.com.au

```html
<!DOCTYPE html>
<html lang="en">
<head>
<meta charset="utf-8">
<title>Velora Pedalworks – Business Card</title>
<link rel="stylesheet" href="https://fonts.googleapis.com/css2?family=Arimo:wght@400;700&display=swap">
<style>
  :root {
    --orange: #f07e00;
    --white: #ffffff;
    --ink: #1c1c1c;
    --backdrop: #e9e6e2;
  }
  * { margin: 0; padding: 0; box-sizing: border-box; }
  html, body {
    width: 1200px;
    height: 918px;
    overflow: hidden;
    background: var(--backdrop);
    font-family: "Arimo", Arial, sans-serif;
  }
  .card {
    position: absolute;
    left: 100px;
    top: 153px;
    width: 1000px;
    height: 611px;
    background: var(--orange);
    overflow: hidden;
    box-shadow: 0 6px 22px rgba(0,0,0,0.18);
  }
  .card-background {
    position: absolute;
    inset: 0;
    width: 100%;
    height: 100%;
  }
  .brand {
    position: absolute;
    right: 42px;
    top: 150px;
    text-align: right;
  }
  .brand-mark {
    display: block;
    width: 52px;
    height: 52px;
    border-radius: 50%;
    background: var(--orange);
    margin: 0 0 14px auto;
  }
  .brand-name {
    font-size: 50px;
    font-weight: 700;
    color: var(--ink);
    letter-spacing: -0.5px;
    line-height: 1;
  }
  .person {
    position: absolute;
    right: 42px;
    top: 282px;
    text-align: right;
  }
  .person-name {
    font-size: 40px;
    font-weight: 700;
    color: var(--ink);
    line-height: 1;
  }
  .person-title {
    font-size: 18px;
    font-weight: 700;
    color: var(--orange);
    margin-top: 4px;
  }
  .contact-list {
    position: absolute;
    left: 60px;
    top: 262px;
    list-style: none;
    color: var(--white);
    font-weight: 700;
    font-size: 26px;
    line-height: 34px;
  }
  .contact-item {
    display: flex;
    align-items: flex-start;
    gap: 22px;
    margin-bottom: 16px;
  }
  .contact-icon {
    flex: none;
    width: 34px;
    height: 34px;
  }
</style>
</head>
<body>
  <div class="card">
    <svg class="card-background" viewBox="0 0 1000 611" aria-hidden="true">
      <path d="M60,0 C250,270 600,410 1000,448 L1000,0 Z" fill="var(--white)"/>
      <path d="M60,0 C250,270 600,410 1000,448" fill="none" stroke="var(--ink)" stroke-width="7"/>
      <path d="M48,0 C240,282 595,424 1000,462" fill="none" stroke="var(--ink)" stroke-width="2"/>
    </svg>

    <div class="brand">
      <span class="brand-mark"></span>
      <div class="brand-name">Velora Pedalworks</div>
    </div>

    <div class="person">
      <div class="person-name">Mavin Tolby</div>
      <div class="person-title">M.D.</div>
    </div>

    <ul class="contact-list">
      <li class="contact-item">
        <svg class="contact-icon" viewBox="0 0 34 34" aria-hidden="true">
          <circle cx="17" cy="17" r="17" fill="var(--white)"/>
          <path d="M17 7 C12.5 7 10 10.5 10 14 C10 19 17 27 17 27 C17 27 24 19 24 14 C24 10.5 21.5 7 17 7 Z" fill="var(--orange)"/>
          <circle cx="17" cy="14" r="3" fill="var(--white)"/>
        </svg>
        <span>PO Box 3862<br>Wattle Crest Corner<br>NSW 2174</span>
      </li>
      <li class="contact-item">
        <svg class="contact-icon" viewBox="0 0 34 34" aria-hidden="true">
          <circle cx="17" cy="17" r="17" fill="var(--white)"/>
          <rect x="11" y="7" width="12" height="20" rx="2" fill="var(--orange)"/>
          <rect x="13" y="10" width="8" height="12" fill="var(--white)"/>
        </svg>
        <span>0438 261 905</span>
      </li>
      <li class="contact-item">
        <svg class="contact-icon" viewBox="0 0 34 34" aria-hidden="true">
          <circle cx="17" cy="17" r="17" fill="var(--white)"/>
          <rect x="8" y="11" width="18" height="12" fill="var(--orange)"/>
          <path d="M8 11 L17 18 L26 11" fill="none" stroke="var(--white)" stroke-width="1.6"/>
        </svg>
        <span>mavin@velorapedalworks.example.com.au</span>
      </li>
      <li class="contact-item">
        <svg class="contact-icon" viewBox="0 0 34 34" aria-hidden="true">
          <circle cx="17" cy="17" r="17" fill="var(--white)"/>
          <circle cx="17" cy="17" r="9" fill="none" stroke="var(--orange)" stroke-width="2"/>
          <ellipse cx="17" cy="17" rx="4" ry="9" fill="none" stroke="var(--orange)" stroke-width="1.6"/>
          <path d="M8 17 H26 M10 12.5 H24 M10 21.5 H24" stroke="var(--orange)" stroke-width="1.4"/>
        </svg>
        <span>www.velorapedalworks.example.com.au</span>
      </li>
    </ul>
  </div>
</body>
</html>
```